New Packaging Design for Olives

We are looking for a new packaging design for our product.
- Clear plastic cup container
- 90mm round lid and tapers down to 45mm base
- We do not want a box
- We would like a cardboard wrap around.
Product:
- Pitted Kalamata Olives
- 90g Net
We would like to product to be displayed from top view and side view.
We would like an image of kalamata olives on the packaging
our logo to appear on top and side
the bottom of the packaging to have room for a bar code, ingredients & nutritional panel.
This product is designed to target the accommodation/hotel market and we are wanting a classy looking design to attract mini bar customers.
Attached is an image of the cup & an internal mock up and our company logo.
We need a design that will seamlessly work across a variety of products including salsa, chilli sauce, tomato sauce and others.
Hotel Mini bar at 4 to 5 star hotels
Hotel

```html
<!DOCTYPE html>
<html lang="en">
<head>
<meta charset="utf-8">
<title>Kalamata Olives Pitted – Wrap Design</title>
<link rel="stylesheet" href="https://fonts.googleapis.com/css2?family=Cinzel:wght@400;600&display=swap">
<style>
  :root {
    --backdrop: #d2d2d2;
    --paper: #ffffff;
    --paper-shade: #ececec;
    --brown-deep: #3b2217;
    --brown-mid: #5e3a2a;
    --brown-warm: #7a4d37;
    --ink-black: #111111;
    --cream: #f6efe6;
    --olive-dark: #4a2a22;
    --olive-light: #8a5a45;
  }
  * { margin: 0; padding: 0; box-sizing: border-box; }
  html, body { width: 1200px; height: 800px; overflow: hidden; }
  body {
    background: var(--backdrop);
    font-family: "Cinzel", "Times New Roman", serif;
  }
  .canvas {
    position: relative;
    width: 1200px;
    height: 800px;
  }
  .wrap-panel {
    position: absolute;
    left: 200px;
    width: 800px;
    height: 300px;
    background: linear-gradient(180deg, var(--paper) 60%, var(--paper-shade));
    overflow: hidden;
    box-shadow: 0 6px 20px rgba(0,0,0,0.18);
  }
  .wrap-panel--top { top: 70px; }
  .wrap-panel--side { top: 400px; }
  .wrap-panel svg.band { position: absolute; inset: 0; }
  .product-title {
    position: absolute;
    left: 60px;
    top: 62px;
    color: var(--cream);
    font-weight: 400;
    font-size: 44px;
    letter-spacing: 1px;
    line-height: 1;
    white-space: nowrap;
    transform: rotate(-4deg);
    transform-origin: left top;
  }
  .product-title .cap { font-size: 56px; }
  .product-variant {
    display: block;
    margin-top: 4px;
    margin-left: 190px;
    font-size: 15px;
    letter-spacing: 8px;
    color: var(--cream);
    opacity: .85;
  }
  .product-photo {
    position: absolute;
    left: 250px;
    top: 140px;
    width: 320px;
    height: 140px;
    border-radius: 50% / 45%;
    background:
      radial-gradient(ellipse at 50% 40%, var(--olive-light) 0%, var(--olive-dark) 55%, rgba(74,42,34,0) 72%),
      radial-gradient(ellipse at 50% 80%, #e9eef0 0%, rgba(233,238,240,0) 70%);
  }
  .brand-name {
    position: absolute;
    right: 36px;
    font-size: 24px;
    font-weight: 600;
    line-height: 1;
  }
  .wrap-panel--top .brand-name { bottom: 18px; color: var(--cream); }
  .wrap-panel--side .brand-name { bottom: 40px; color: var(--brown-deep); }
  .net-weight {
    position: absolute;
    left: 28px;
    top: 26px;
    color: var(--cream);
    font-size: 14px;
    letter-spacing: 1px;
    transform: rotate(-8deg);
    transform-origin: left top;
  }
</style>
</head>
<body>
<main class="canvas">

  <section class="wrap-panel wrap-panel--top">
    <svg class="band" width="800" height="300" viewBox="0 0 800 300" aria-hidden="true">
      <defs>
        <linearGradient id="bandBrownTop" x1="0" y1="0" x2="1" y2="0">
          <stop offset="0" stop-color="#3b2217"/>
          <stop offset=".5" stop-color="#7a4d37"/>
          <stop offset="1" stop-color="#5e3a2a"/>
        </linearGradient>
      </defs>
      <path d="M0 0 H800 V140 Q420 110 0 215 Z" fill="url(#bandBrownTop)"/>
      <path d="M800 215 Q560 218 360 300 H800 Z" fill="#111111"/>
    </svg>
    <h2 class="product-title"><span class="cap">K</span>ALAMATA <span class="cap">O</span>LIVES<span class="product-variant">PITTED</span></h2>
    <div class="product-photo" role="img" aria-label="Pitted kalamata olives in a clear glass bowl with a rosemary sprig"></div>
    <p class="brand-name">Harrow's</p>
  </section>

  <section class="wrap-panel wrap-panel--side">
    <svg class="band" width="800" height="300" viewBox="0 0 800 300" aria-hidden="true">
      <defs>
        <linearGradient id="bandBrownSide" x1="0" y1="0" x2="1" y2="0">
          <stop offset="0" stop-color="#3b2217"/>
          <stop offset=".5" stop-color="#7a4d37"/>
          <stop offset="1" stop-color="#5e3a2a"/>
        </linearGradient>
      </defs>
      <path d="M0 0 H800 V140 Q420 110 0 215 Z" fill="url(#bandBrownSide)"/>
      <path d="M0 0 H420 Q200 20 0 70 Z" fill="#111111"/>
    </svg>
    <p class="net-weight">90g NET</p>
    <h2 class="product-title"><span class="cap">K</span>ALAMATA <span class="cap">O</span>LIVES<span class="product-variant">PITTED</span></h2>
    <div class="product-photo" role="img" aria-label="Pitted kalamata olives in a clear glass bowl with a rosemary sprig"></div>
    <p class="brand-name">Harrow's</p>
  </section>

</main>
</body>
</html>
```